Local Finance and Insurance Advising Company from Switzerland needs an impressive banner design.

I am looking for an impressive Banner Design, I need this Banner for Facebook, LinkedIn, YouTube & Google.

I am Advising all kind of peoples who are living here in Switzerland. Young, middle age and old people. People who want to go study, people who are planning to create a family, old people who are, or going to retire. Expatriates who want to leave Switzerland to live in another country, expatriates who are coming to Switzerland. Peoples who ant to build their own business up. All kind of financial, insurance and pension planning's.

The Company Name is: Alpine Counsel
Our slogen / heading is: Clear Guidance, no Pitch

The Company logo can be used for the banner, but I would preffer to have the banner without logo, as the logo will be already in a another field on the social networks.

Since the first impression is the most important, this project is really important to me. I am ready to realize further projects with the one who can create the perfect banner who hits the point as described. I am a start-up company, everything is still on beginning and still much has to be done.

Target Market(s)

private clients

Requirements
Must have
• The banner should give the impression of happiness, safeness, health and freedom. Empowering people and creating freedom lifestyles.
Should not have
• I do not want that the banner looks like we are some kind of broker who is just selling some kind of insurances.

```html
<!DOCTYPE html>
<html lang="en">
<head>
<meta charset="utf-8">
<title>Empowering People – Banner Samples</title>
<link rel="stylesheet" href="https://fonts.googleapis.com/css2?family=Bebas+Neue&family=Quicksand:wght@500&display=swap">
<style>
  :root {
    --sheet-bg: #232323;
    --label-grey: #4b4b4b;
    --mauve: #7b5b67;
    --red: #e70f1f;
    --sky-top: #fffaf3;
    --sky-mid: #fdeee4;
    --field-orange: #f2a046;
    --field-deep: #c7672c;
    --figure-pink: #e9b2b0;
    --figure-rose: #d98f8c;
    --figure-dusk: #4a3340;
  }
  * { margin: 0; padding: 0; box-sizing: border-box; }
  html, body {
    width: 1200px;
    height: 2183px;
    overflow: hidden;
    background: var(--sheet-bg);
  }
  .sheet { position: relative; width: 1200px; height: 2183px; }

  .sample-label {
    position: absolute;
    left: 0;
    width: 1200px;
    text-align: center;
    font-family: "Bebas Neue", sans-serif;
    font-weight: 400;
    font-size: 68px;
    line-height: 1;
    letter-spacing: 1px;
    color: var(--label-grey);
  }

  .banner {
    position: absolute;
    left: 108px;
    width: 984px;
    height: 374px;
    overflow: hidden;
  }
  .banner-sky {
    position: absolute;
    inset: 0;
    background:
      radial-gradient(ellipse 60% 22% at 30% 100%, rgba(199,103,44,0.6), rgba(199,103,44,0) 80%),
      linear-gradient(180deg, var(--sky-top) 0%, var(--sky-mid) 68%, var(--field-orange) 86%, var(--field-deep) 100%);
  }
  .banner-photo {
    position: absolute;
    left: 610px;
    top: 0;
    width: 374px;
    height: 374px;
    background:
      linear-gradient(180deg, rgba(233,178,176,0) 0%, rgba(233,178,176,0) 70%, var(--figure-dusk) 100%),
      linear-gradient(135deg, #f7d9d4 0%, var(--figure-pink) 45%, var(--figure-rose) 100%);
  }

  .headline {
    position: absolute;
    left: 46px;
    top: 86px;
    font-family: "Bebas Neue", sans-serif;
    font-weight: 400;
    font-size: 86px;
    line-height: 1;
    white-space: nowrap;
    color: var(--mauve);
  }
  .headline.is-red { color: var(--red); }

  .tagline {
    position: absolute;
    left: 66px;
    top: 166px;
    font-family: "Quicksand", sans-serif;
    font-weight: 500;
    font-size: 34px;
    line-height: 41px;
    color: var(--red);
  }
  .tagline.is-mauve { color: var(--mauve); }
  .tagline.single-line { left: 46px; top: 162px; white-space: nowrap; }

  .accent-bar {
    position: absolute;
    left: 49px;
    top: 173px;
    width: 4px;
    height: 73px;
    background: var(--red);
  }
  .accent-bar.is-mauve { background: var(--mauve); }
  .accent-underline {
    position: absolute;
    left: 46px;
    top: 216px;
    width: 71px;
    height: 4px;
    background: var(--red);
  }
</style>
</head>
<body>
<main class="sheet">

  <h2 class="sample-label" style="top:46px">Sample - 01</h2>
  <section class="banner" style="top:139px">
    <div class="banner-sky"></div>
    <div class="banner-photo" role="img" aria-label="Photo of a young woman with open arms in a sunlit field at sunset"></div>
    <h1 class="headline">Empowering People</h1>
    <span class="accent-bar"></span>
    <p class="tagline">Creating Freedom<br>Lifestyle</p>
  </section>

  <h2 class="sample-label" style="top:572px">Sample - 02</h2>
  <section class="banner" style="top:677px">
    <div class="banner-sky"></div>
    <div class="banner-photo" role="img" aria-label="Photo of a young woman with open arms in a sunlit field at sunset"></div>
    <h1 class="headline is-red">Empowering People</h1>
    <span class="accent-bar"></span>
    <p class="tagline">Creating Freedom<br>Lifestyle</p>
  </section>

  <h2 class="sample-label" style="top:1122px">Sample - 03</h2>
  <section class="banner" style="top:1226px">
    <div class="banner-sky"></div>
    <div class="banner-photo" role="img" aria-label="Photo of a young woman with open arms in a sunlit field at sunset"></div>
    <h1 class="headline">Empowering People</h1>
    <p class="tagline single-line">Creating Freedom Lifestyle</p>
    <span class="accent-underline"></span>
  </section>

  <h2 class="sample-label" style="top:1652px">Sample - 04</h2>
  <section class="banner" style="top:1750px">
    <div class="banner-sky"></div>
    <div class="banner-photo" role="img" aria-label="Photo of a young woman with open arms in a sunlit field at sunset"></div>
    <h1 class="headline is-red">Empowering People</h1>
    <span class="accent-bar is-mauve"></span>
    <p class="tagline is-mauve">Creating Freedom<br>Lifestyle</p>
  </section>

</main>
</body>
</html>
```